It must be unique & Proffessional
VORNA GROUP
# 130 Very nice, could you please use the “symbols” for Phone, cellphone and so on, instead of writing “p:” and “c:”. You did that by # 69 :-)
Thanks for all your very creative suggestions.
A general comment:
- Please correct the “projektchef” to “Direktør”
- Please add at fixed telephone number +45 62 18 37 51
- Please add “+45” in front of the cellphone number
- Please make the envelope as window envelops, and logo bottom right corner
- On the A4 paper, we need the logo in top right corner
#61,Very good design, please make the backside as you’ve done by #64
#128Please leave the bottom of the paper free of text and colors, and add only one thin line 13 mm from the page bottom.
Again very good designs, thank you very much
Logo AI file is now uploaded :-)
Now we have our Logo ready, looking forward to see your suggestions for design :-)
TK/RWF Team
Logo is currently being designed, you can participate if you would like to :-)

```html
<!DOCTYPE html>
<html lang="da">
<head>
<meta charset="utf-8">
<title>VORNA GROUP – Stationery</title>
<link href="https://fonts.googleapis.com/css2?family=Oswald:wght@500&family=Open+Sans:wght@400;600&display=swap" rel="stylesheet">
<style>
  :root{
    --bg:#ffffff;
    --frame:#e4e4e4;
    --paper:#ffffff;
    --navy:#34506f;
    --accent:#c63b3b;
    --ink:#5a6470;
    --rule:#8a97a6;
    --shadow:rgba(0,0,0,.28);
  }
  *{box-sizing:border-box;margin:0;padding:0}
  html,body{width:1200px;height:681px;overflow:hidden;background:var(--bg)}
  .canvas{position:relative;width:1200px;height:681px;font-family:"Open Sans",Arial,sans-serif;color:var(--ink)}
  .frame{position:absolute;left:22px;top:22px;width:1156px;height:637px;border:1px solid var(--frame)}
  .sheet{position:absolute;background:var(--paper);box-shadow:3px 4px 8px var(--shadow)}

  .brand{display:flex;flex-direction:column;align-items:center;line-height:1}
  .brand-row{display:flex;align-items:center;gap:5px}
  .brand-mark{width:9px;height:9px;background:var(--accent)}
  .brand-name{font-family:"Oswald",Arial,sans-serif;font-weight:500;color:var(--navy);letter-spacing:.5px}
  .brand-sub{font-family:"Open Sans",Arial,sans-serif;font-weight:600;color:var(--navy);letter-spacing:2px;margin-top:2px}

  .contact-line{display:flex;flex-direction:column;align-items:center;gap:3px;font-size:5.5px;color:var(--ink)}
  .contact-line .addr{display:flex;align-items:center;gap:6px}
  .contact-line .addr::before,.contact-line .addr::after{content:"";width:44px;height:1px;background:var(--rule)}

  /* envelope front */
  .env-front{left:60px;top:96px;width:420px;height:216px}
  .env-front .brand{position:absolute;left:22px;top:18px}
  .env-front .brand-name{font-size:19px}
  .env-front .brand-sub{font-size:6px}
  .env-front .contact-line{position:absolute;left:0;right:0;bottom:14px}

  /* envelope back */
  .env-back{left:60px;top:360px;width:420px;height:216px}
  .env-back svg{position:absolute;left:0;top:0}
  .env-back .brand{position:absolute;left:0;right:0;top:46px}
  .env-back .brand-name{font-size:11px}

  /* letterhead */
  .letter{left:624px;top:48px;width:312px;height:576px}
  .letter .brand{position:absolute;left:0;right:0;top:46px}
  .letter .brand-name{font-size:21px}
  .letter .brand-sub{font-size:6.5px}
  .letter .contact-line{position:absolute;left:0;right:0;bottom:18px}

  /* business cards */
  .card-front{left:965px;top:144px;width:211px;height:108px}
  .card-front .brand{position:absolute;left:0;right:0;top:14px}
  .card-front .brand-name{font-size:13px}
  .card-front .brand-sub{font-size:4.5px}
  .card-front .person{position:absolute;left:0;right:0;top:58px;text-align:center;font-size:6px;color:var(--navy);font-weight:600}
  .card-front .role{display:block;font-weight:400;font-size:4.5px;color:var(--ink);margin-top:1px}
  .card-front .contact-line{position:absolute;left:0;right:0;bottom:18px;font-size:4.2px}
  .card-front .contact-line .addr::before,.card-front .contact-line .addr::after{width:22px}

  .card-back{left:965px;top:269px;width:211px;height:108px;display:flex;align-items:center;justify-content:center}
  .card-back .brand-name{font-size:12px}
</style>
</head>
<body>
<main class="canvas">
  <div class="frame"></div>

  <section class="sheet env-front" aria-label="Envelope front">
    <div class="brand">
      <div class="brand-row"><span class="brand-mark"></span><span class="brand-name">VORNA GROUP</span></div>
      <span class="brand-sub">DEVELOPMENT</span>
    </div>
    <div class="contact-line">
      <span class="addr">Haldsvej 31 | 7100 Vejle</span>
      <span>Call: +45 62 18 37 51 | Email: info@vornagroup.com | www.vornagroup.com</span>
    </div>
  </section>

  <section class="sheet env-back" aria-label="Envelope back">
    <svg width="420" height="216" viewBox="0 0 420 216">
      <path d="M4 4 Q6 22 24 30 L196 86 Q210 90 224 86 L396 30 Q414 22 416 4" fill="none" stroke="#9aa2ab" stroke-width="1"/>
    </svg>
    <div class="brand">
      <div class="brand-row"><span class="brand-name">VORNA GROUP</span></div>
    </div>
  </section>

  <section class="sheet letter" aria-label="Letterhead">
    <div class="brand">
      <div class="brand-row"><span class="brand-mark"></span><span class="brand-name">VORNA GROUP</span></div>
      <span class="brand-sub">DEVELOPMENT</span>
    </div>
    <div class="contact-line">
      <span class="addr">Haldsvej 31 | 7100 Vejle</span>
      <span>Call: +45 62 18 37 51 | Email: info@vornagroup.com | www.vornagroup.com</span>
    </div>
  </section>

  <section class="sheet card-front" aria-label="Business card front">
    <div class="brand">
      <div class="brand-row"><span class="brand-mark"></span><span class="brand-name">VORNA GROUP</span></div>
      <span class="brand-sub">DEVELOPMENT</span>
    </div>
    <p class="person">Jonas Morpvelto<span class="role">Direktør</span></p>
    <div class="contact-line">
      <span class="addr">Haldsvej 31 | 7100 Vejle</span>
      <span>+45 62 18 37 51 | jm@vornagroup.com | www.vornagroup.com</span>
    </div>
  </section>

  <section class="sheet card-back" aria-label="Business card back">
    <span class="brand-name">VORNA GROUP</span>
  </section>
</main>
</body>
</html>
```